International pain relief company needs flyer designed

We are based in South Australia, and are about to launch a brand new hand held portable fully chargeable pain relief device. This device gives the user proven instant relief often from the first time of use anywhere. We intend to offer, a try before you buy at home /office demonstration, a full 30 day money back guarantee and a full 3 year warranty. We also plan to give the first 7 people who book a demonstration a FREE $20 Norvane fuel card.
We are open minded regarding the overall design and colours used, however we are particularly keen on seeing pictures/cartoons of people suffering from the 3 main groups of pain, head ache, back ache and joint pain, perhaps also happy faces once they have been cured/relieved by our equipment. This product we expect to retail for around the $300 AUD mark.
The wording on the leaflet is
Suffering from headaches, back ache or joint problems?
At last....there is instant pain relief!
New to Australia, a personal portable pain relief device
Call Ted 0427586193 & 08 72514938
RWP Australia PO Box 618, Fernleigh SA 5094

Target Market(s)

aged, elderly

Industry/Entity Type

Retail

Font styles to use
Serif
Sans Serif

Colors
33b7a4
33a6d7
3176b5

Requirements
Must have
• include Free in house/office demonstration
Free $20 Norvan fuel card for first 11 demonstrations
Nice to have
• Norvane fuel logo

```html
<!DOCTYPE html>
<html lang="en">
<head>
<meta charset="utf-8">
<title>Instant Pain Relief Flyer</title>
<link href="https://fonts.googleapis.com/css2?family=Oswald:wght@500;600;700&display=swap" rel="stylesheet">
<style>
:root{
  --blue-deep:#1b3fae;
  --blue-mid:#2a78e4;
  --blue-light:#3fa0f5;
  --orange-hot:#e8561a;
  --orange:#f7861f;
  --orange-light:#fba24a;
  --ink:#141414;
  --white:#ffffff;
  --ring:#c9ccd3;
  --badge:#1d55d6;
  --brand-red:#c8202f;
}
*{margin:0;padding:0;box-sizing:border-box}
html,body{width:933px;height:1200px;overflow:hidden;background:var(--blue-deep)}
.canvas{
  position:relative;width:875px;height:1125px;
  transform:scale(1.0664);transform-origin:0 0;overflow:hidden;
  background:radial-gradient(ellipse 70% 60% at 48% 52%, var(--blue-light) 0%, var(--blue-mid) 45%, var(--blue-deep) 100%);
  font-family:'Oswald',Impact,sans-serif;font-weight:700;color:var(--ink);
  text-transform:uppercase;letter-spacing:0.2px;
}
.banner{
  position:absolute;border-radius:26px;
  background:linear-gradient(90deg,var(--orange-hot),var(--orange) 55%,var(--orange-light));
  box-shadow:4px 6px 0 rgba(0,0,0,.35);
}
.banner--top{left:290px;top:100px;width:555px;height:198px}
.banner--mid{left:30px;top:370px;width:580px;height:195px;
  background:linear-gradient(90deg,var(--orange-light),var(--orange) 45%,var(--orange-hot))}
.line{position:absolute;text-align:center;white-space:nowrap;line-height:1}
.headline{left:290px;width:555px;font-size:47px}
.relief{left:30px;width:480px;font-size:42px}
.subline{left:30px;width:510px;font-size:29px}
.photo{
  position:absolute;border-radius:50%;border:7px solid var(--ring);
  box-shadow:0 0 0 2px var(--white) inset, 2px 4px 8px rgba(0,0,0,.35);
}
.photo--head{left:33px;top:48px;width:142px;height:142px;background:radial-gradient(circle at 40% 40%,#f3d9b8,#d9a88a 60%,#e07aa6)}
.photo--knee{left:193px;top:62px;width:155px;height:155px;background:radial-gradient(circle at 55% 50%,#d9a07e,#b9755a 55%,#3a3a3a)}
.photo--back{left:103px;top:192px;width:158px;height:158px;background:radial-gradient(circle at 45% 45%,#d6473a 0%,#c98b70 30%,#a86a52 70%,#f3f1ee)}
.photo--woman{left:508px;top:333px;width:145px;height:145px;background:radial-gradient(circle at 50% 45%,#f2cfa8,#e2b98a 45%,#cfe3ea)}
.photo--elders{left:673px;top:330px;width:150px;height:150px;background:radial-gradient(circle at 50% 55%,#f0d0b8,#d9c6b6 45%,#e8eaec)}
.photo--couple{left:600px;top:456px;width:160px;height:160px;background:radial-gradient(circle at 50% 50%,#e3a88a,#a34a3c 55%,#8b8f8a)}
.offer{left:0;width:660px;color:var(--white);font-weight:600}
.offer--big{font-size:25px}
.offer--small{font-size:22px}
.badge{
  position:absolute;left:568px;top:682px;width:174px;height:174px;border-radius:50%;
  background:radial-gradient(circle at 45% 40%,#3a78ee,var(--badge) 70%);
  border:6px solid var(--white);box-shadow:2px 4px 8px rgba(0,0,0,.4);
  color:var(--white);
  display:flex;align-items:center;justify-content:center;overflow:hidden;
}
.badge__text{transform:rotate(15deg) translate(2px,-4px);text-align:center;line-height:.9}
.badge__top{display:flex;align-items:center;justify-content:center;gap:3px}
.badge__num{font-size:60px;line-height:.8}
.badge__stack{font-size:24px;line-height:.9;text-align:left}
.badge__line{display:block;font-size:17px;line-height:1}
.brand-mark{
  position:absolute;left:660px;top:828px;width:176px;height:176px;border-radius:50%;
  background:var(--white);border:6px solid var(--ring);box-shadow:2px 4px 8px rgba(0,0,0,.4);
  display:flex;align-items:center;justify-content:center;
  font-size:30px;color:var(--brand-red);letter-spacing:1px;
}
.footer-arc{position:absolute;left:0;top:0}
.footer{left:0;width:620px;font-size:25px}
.footer .hi{color:var(--white)}
.footer--call{font-size:26px}
.divider{position:absolute;left:165px;width:290px;border-top:2px dotted var(--white)}
.conditions{
  position:absolute;left:612px;top:1010px;font-size:11px;color:var(--white);
  transform:rotate(62deg);transform-origin:left top;white-space:nowrap;
}
</style>
</head>
<body>
<div class="canvas">
  <div class="banner banner--top"></div>
  <div class="line headline" style="top:120px">Suffering from</div>
  <div class="line headline" style="top:178px">headaches, back ache</div>
  <div class="line headline" style="top:236px">or joint problems?</div>

  <div class="photo photo--knee" role="img" aria-label="Photo of hands holding a sore knee"></div>
  <div class="photo photo--head" role="img" aria-label="Photo of a woman with a headache"></div>
  <div class="photo photo--back" role="img" aria-label="Photo of a man with lower back pain"></div>

  <div class="banner banner--mid"></div>
  <div class="line relief" style="top:382px">At last....there is</div>
  <div class="line relief" style="top:430px">instant pain relief!</div>
  <div class="line subline" style="top:486px">A personal, portable pain relief</div>
  <div class="line subline" style="top:520px">device, new to Australia!</div>

  <div class="photo photo--woman" role="img" aria-label="Photo of a smiling young woman"></div>
  <div class="photo photo--elders" role="img" aria-label="Photo of a happy elderly couple"></div>
  <div class="photo photo--couple" role="img" aria-label="Photo of a smiling middle-aged couple"></div>

  <div class="line offer offer--big" style="top:582px">* Free in home/office demonstrations</div>
  <div class="line offer offer--small" style="top:612px">(takes 20 minutes)</div>
  <div class="line offer offer--big" style="top:648px">* A full 30 day money back, no quibble guarantee</div>
  <div class="line offer offer--small" style="top:678px">(if you are not delighted with the results)</div>
  <div class="line offer offer--big" style="top:716px">* Various accessories available</div>
  <div class="line offer offer--big" style="top:753px">*Some health insurance rebates*</div>

  <div class="badge">
    <div class="badge__text">
      <div class="badge__top">
        <span class="badge__num">3</span>
        <span class="badge__stack">*Full<br>year</span>
      </div>
      <span class="badge__line">manufacturers</span>
      <span class="badge__line">warranty.</span>
    </div>
  </div>

  <svg class="footer-arc" width="875" height="1125" viewBox="0 0 875 1125" aria-hidden="true">
    <defs>
      <linearGradient id="arcFill" x1="0" y1="0" x2="1" y2="1">
        <stop offset="0" stop-color="#f7941d"/>
        <stop offset="1" stop-color="#e64d12"/>
      </linearGradient>
    </defs>
    <path d="M0 895 C 170 805, 460 755, 610 850 C 700 910, 745 1010, 748 1125 L0 1125 Z" fill="url(#arcFill)" stroke="#111" stroke-width="6"/>
  </svg>

  <div class="brand-mark">Norvane</div>

  <div class="line footer" style="top:820px">First <span class="hi">7</span> people</div>
  <div class="line footer" style="top:850px">to book a demonstration</div>
  <div class="line footer" style="top:882px">receive a <span class="hi">free $20</span> Norvane fuel card*</div>
  <div class="divider" style="top:918px"></div>
  <div class="line footer footer--call" style="top:932px"><span class="hi">Call</span> Ted 0427586193 and 08 72514938</div>
  <div class="divider" style="top:972px"></div>
  <div class="line footer" style="top:985px">www.easeworldrelief.com.au</div>
  <div class="divider" style="top:1022px"></div>
  <div class="line footer" style="top:1034px">RWP Australia Pty Ltd,</div>
  <div class="line footer" style="top:1064px">PO Box 618, Fernleigh SA</div>

  <div class="conditions">*Some conditions apply</div>
</div>
</body>
</html>
```